Naturopath needs product label for new essence range

I need a label design for a new range of Essences. The essences resonate with the energetic chakra centres of the body to shift blockages, balance them and lead to transformation and spiritual growth. I have a logo to be used. The name of the essence range is Veloria which means "to reveal truth or True Nature". The first essence resonates with the Base Chakra and is called "Base" I would like a strong bold red colour to feature in the design. The label size would be about 76mm x 27mm. See below for the required information to be on the label.
Updates

Hi everyone, I'm not sure if it's important to help with the design, but I've just uploaded the logo in several different formats. Thanks for all your submissions. Also please use a deep red colour, the example from the colour wheel is too light. Kind regards, Brent

Target Market(s)

Adults open to alternative therapies and spiritual development

Industry/Entity Type

Product

Colors
eb1f27

Requirements
Must have
• The logo. A deep red colour as the background or part of the background
"Base"
veloriadrops.com.au
Batch
Expiry
Ingredients: vibrational essence of herbs, flowers and crystals, purified water, brandy (approx 12.5% alcohol)
20ml
Dosage: 7 drops once a day

```html
<!DOCTYPE html>
<html lang="en">
<head>
<meta charset="utf-8">
<title>Veloria Essences – Base label</title>
<link rel="stylesheet" href="https://fonts.googleapis.com/css2?family=Tinos&family=Questrial&display=swap">
<style>
  :root {
    --backdrop: #2a2a2a;
    --deep-red-edge: #6a0c11;
    --deep-red-core: #9c1a20;
    --bright-red-edge: #a81c22;
    --bright-red-core: #e41f27;
    --gold-light: #f8c47c;
    --gold-head: #e9a05a;
    --gold-mark: #d6a33c;
    --gold-dark: #9a6a22;
    --gold-pale: #f6e2b8;
    --body-text: #f0d9d6;
    --logo-black: #060708;
  }
  * { box-sizing: border-box; margin: 0; padding: 0; }
  html, body { width: 1200px; height: 1000px; overflow: hidden; }
  body {
    background: var(--backdrop);
    position: relative;
    font-family: "Questrial", "Century Gothic", sans-serif;
  }
  .label {
    position: absolute;
    width: 1080px;
    height: 383px;
    border-radius: 28px;
    overflow: hidden;
  }
  .label--deep {
    left: 66px; top: 97px;
    background: linear-gradient(90deg, var(--deep-red-edge) 0%, var(--deep-red-core) 50%, var(--deep-red-edge) 100%);
  }
  .label--bright {
    left: 70px; top: 524px;
    background: linear-gradient(90deg, var(--bright-red-edge) 0%, var(--bright-red-core) 50%, var(--bright-red-edge) 100%);
  }
  .product-name {
    position: absolute;
    left: 0; right: 0; top: 18px;
    margin-left: 10px;
    text-align: center;
    font-family: "Tinos", "Times New Roman", serif;
    font-size: 51px;
    font-weight: 400;
    color: var(--gold-light);
    letter-spacing: 0.5px;
  }
  .logo-panel {
    position: absolute;
    left: 58px; top: 75px;
    width: 294px; height: 222px;
    background: var(--logo-black);
    display: flex; align-items: center; justify-content: center;
  }
  .label--deep .logo-panel { border: 4px solid var(--gold-light); }
  .label--bright .logo-panel {
    border: 4px solid transparent;
    background:
      linear-gradient(var(--logo-black), var(--logo-black)) padding-box,
      linear-gradient(135deg, var(--gold-dark), var(--gold-pale) 45%, var(--gold-dark) 70%, var(--gold-pale)) border-box;
  }
  .logo-name {
    font-family: "Tinos", "Times New Roman", serif;
    font-size: 30px;
    font-weight: 400;
    color: var(--gold-mark);
  }
  .figure-art {
    position: absolute;
    left: 432px; top: 91px;
    width: 214px; height: 190px;
  }
  .volume {
    position: absolute;
    left: 0; right: 0; top: 303px;
    margin-left: 8px;
    text-align: center;
    font-size: 20px;
    color: var(--body-text);
  }
  .details {
    position: absolute;
    left: 738px; top: 72px;
    width: 330px;
    font-size: 20px;
    line-height: 24px;
    color: var(--body-text);
  }
  .details dt {
    font-size: 18px;
    font-weight: 700;
    color: var(--gold-head);
    text-transform: uppercase;
  }
  .details .ingredients-list { margin-bottom: 15px; }
  .details .dosage-amount { margin-bottom: 10px; }
  .footer-band {
    position: absolute;
    left: 0; right: 0; top: 347px;
    height: 16px;
    display: flex; align-items: center;
  }
  .footer-band .rule { flex: 1; height: 8px; }
  .label--deep .rule { background: var(--gold-light); }
  .label--bright .rule--left { background: linear-gradient(90deg, var(--gold-dark), var(--gold-mark) 60%, var(--gold-pale)); }
  .label--bright .rule--right { background: linear-gradient(90deg, var(--gold-mark), var(--gold-pale) 60%, var(--gold-dark)); }
  .website {
    padding: 0 8px;
    font-family: "Tinos", "Times New Roman", serif;
    font-size: 22px;
    letter-spacing: 1px;
    color: var(--gold-light);
  }
</style>
</head>
<body>

<section class="label label--deep">
  <h1 class="product-name">BASE</h1>
  <div class="logo-panel">
    <span class="logo-name">Veloria</span>
  </div>
  <svg class="figure-art" role="img" aria-label="Silhouette of a seated meditating figure" viewBox="0 0 214 190">
    <ellipse cx="107" cy="110" rx="104" ry="78" fill="#ffffff" fill-opacity="0.18"/>
  </svg>
  <p class="volume">20ml</p>
  <dl class="details">
    <dt>Ingredients</dt>
    <dd class="ingredients-list">vibrational essence of herbs<br>flowers and crystals<br>purified water<br>brandy (approx 12.5% alcohol)</dd>
    <dt>Dosage</dt>
    <dd class="dosage-amount">7 drops once a day</dd>
    <dt>Batch</dt>
    <dt>Expiry</dt>
  </dl>
  <div class="footer-band">
    <span class="rule rule--left"></span>
    <span class="website">veloriadrops.com.au</span>
    <span class="rule rule--right"></span>
  </div>
</section>

<section class="label label--bright">
  <h1 class="product-name">BASE</h1>
  <div class="logo-panel">
    <span class="logo-name">Veloria</span>
  </div>
  <svg class="figure-art" role="img" aria-label="Silhouette of a seated meditating figure" viewBox="0 0 214 190">
    <ellipse cx="107" cy="110" rx="104" ry="78" fill="#ffffff" fill-opacity="0.2"/>
  </svg>
  <p class="volume">20ml</p>
  <dl class="details">
    <dt>Ingredients</dt>
    <dd class="ingredients-list">vibrational essence of herbs<br>flowers and crystals<br>purified water<br>brandy (approx 12.5% alcohol)</dd>
    <dt>Dosage</dt>
    <dd class="dosage-amount">7 drops once a day</dd>
    <dt>Batch</dt>
    <dt>Expiry</dt>
  </dl>
  <div class="footer-band">
    <span class="rule rule--left"></span>
    <span class="website">veloriadrops.com.au</span>
    <span class="rule rule--right"></span>
  </div>
</section>

</body>
</html>
```